Refresh of The Marwick Partners business card

Update business card design using existing primary logo. Names, numbers, etc. are too hard to read on current design.

Target Market(s)

We are a CPA firm.

Industry/Entity Type

Accountant

Contact Information for Business Card

update current card

Colors
0355a3
3176b5
85acd3
0792cd

Requirements
Must have
• Easier to read phone numbers and names
• Use existing logo
Nice to have
• We love our color scheme and current TMP logo. But the names and phone numbers are too small and card just look old and stale.

```html
<!DOCTYPE html>
<html lang="en">
<head>
<meta charset="utf-8">
<title>The Marwick Partners — Business Card</title>
<link rel="stylesheet" href="https://fonts.googleapis.com/css2?family=Cinzel:wght@600&family=Open+Sans:wght@400;600&display=swap">
<style>
  :root {
    --bg: #2e2927;
    --card: #141516;
    --card-edge: #1d1e20;
    --silver: #8d8f93;
    --silver-light: #b9bbbf;
    --text: #e6e7e9;
    --brand-blue: #0355a3;
    --brand-mid: #3176b5;
    --brand-light: #85acd3;
    --brand-cyan: #0792cd;
  }
  * { box-sizing: border-box; margin: 0; padding: 0; }
  html, body { width: 1200px; height: 864px; overflow: hidden; }
  body {
    background: var(--bg);
    font-family: "Open Sans", Arial, sans-serif;
    display: flex; align-items: center; justify-content: center; gap: 40px;
  }
  .card {
    width: 540px; height: 309px;
    background: var(--card);
    border: 1px solid var(--card-edge);
    box-shadow: 0 14px 30px rgba(0,0,0,.45);
    position: relative;
  }
  /* Front */
  .card-front .brand {
    position: absolute; left: 120px; top: 88px;
    display: flex; align-items: center; gap: 18px;
  }
  .brand-dot {
    width: 76px; height: 76px; border-radius: 50%;
    background: var(--silver);
  }
  .brand-name {
    font-family: "Cinzel", Georgia, serif; font-weight: 600;
    color: var(--silver-light); font-size: 26px; line-height: 1.1;
    letter-spacing: 1px;
  }
  .brand-tagline {
    margin-top: 6px; font-size: 9px; letter-spacing: 2.5px;
    text-transform: uppercase; color: var(--silver); font-weight: 600;
  }
  .website {
    position: absolute; left: 0; right: 0; bottom: 62px; text-align: center;
    font-size: 13px; letter-spacing: 3px; color: var(--silver);
  }
  /* Back */
  .card-back .seal {
    position: absolute; left: 48px; top: 58px; width: 170px;
    display: flex; flex-direction: column; align-items: center; gap: 14px;
  }
  .seal-circle {
    width: 150px; height: 150px; border-radius: 50%;
    background: var(--brand-mid);
    border: 5px solid #5d6066;
  }
  .seal-name {
    font-size: 14px; font-weight: 600; color: var(--brand-light);
    letter-spacing: .5px; text-align: center;
  }
  .divider {
    position: absolute; left: 246px; top: 42px; bottom: 42px; width: 1px;
    background: linear-gradient(var(--card), #9a9ca0 50%, var(--card));
  }
  .contact {
    position: absolute; left: 272px; top: 74px; color: var(--text);
    font-size: 15px; line-height: 1.35;
  }
  .contact-name {
    color: var(--brand-cyan); font-weight: 600; font-size: 17px;
    text-transform: uppercase; margin-bottom: 8px;
  }
  .contact-address { margin-bottom: 6px; }
  .contact-line { display: flex; align-items: center; gap: 9px; }
  .contact-line svg { width: 13px; height: 13px; fill: var(--brand-mid); flex: none; }
</style>
</head>
<body>
  <section class="card card-front">
    <div class="brand">
      <div class="brand-dot"></div>
      <div>
        <div class="brand-name">The Marwick<br>Partners</div>
        <div class="brand-tagline">Certified Public Accountants</div>
      </div>
    </div>
    <div class="website">www.marwickpartners.com</div>
  </section>

  <section class="card card-back">
    <div class="seal">
      <div class="seal-circle"></div>
      <div class="seal-name">The Marwick Partners</div>
    </div>
    <div class="divider"></div>
    <div class="contact">
      <div class="contact-name">Daniel R. Marwick, CPA</div>
      <div class="contact-address">318 N. Lakeview Rd. Suite 112<br>Oviedo, Florida 32765</div>
      <div class="contact-line">
        <svg viewBox="0 0 16 16" aria-hidden="true"><path d="M1 5q7-5 14 0v2h-4V5.5H5V7H1zM3 8h10l1 6H2z"/></svg>
        <span>407.555.0142</span>
      </div>
      <div class="contact-line">
        <svg viewBox="0 0 16 16" aria-hidden="true"><path d="M4 1h8v14H4zM5.5 3v9h5V3z"/></svg>
        <span>407.555.0187</span>
      </div>
      <div class="contact-line">
        <svg viewBox="0 0 16 16" aria-hidden="true"><path d="M4 1h7v4H4zM1 6h14v7H1zM4 11h8v4H4z"/></svg>
        <span>407.555.0163</span>
      </div>
      <div class="contact-line">
        <svg viewBox="0 0 16 16" aria-hidden="true"><path d="M1 3h14v10H1zM2 4l6 5 6-5z"/></svg>
        <span>dan@marwickpartners.com</span>
      </div>
    </div>
  </section>
</body>
</html>
```